Stanbrook Fire Services Pty Ltd

We need business cards for a company based in Perth, we install, service and maintain fire equipment.
On the front we want a great design with our logo and a small spot for our full company name, general company email address and office number. On the back we need space for our name, title, mobile number and email address on the back.

Target Market(s)

Facility managers and commercial/industrial building owners/occupiers.

Contact Information for Business Card

Font styles to use
Sans Serif

Requirements
Must have
• Please only submit 5 of your best samples.
Darker tones are preferred.
Nice to have
• We want to use, black, red and grey. Keep it modern and clean.
I've attached the company logo and a sample of a boarder we use on our emergency plans.
Should not have
• No preference. Let the designer choose.

```html
<!DOCTYPE html>
<html lang="en">
<head>
<meta charset="utf-8">
<title>Stanbrook Fire Services – Business Cards</title>
<link href="https://fonts.googleapis.com/css2?family=Montserrat:wght@700;800&family=Arimo:wght@400;700&display=swap" rel="stylesheet">
<style>
  :root {
    --stage: #2b2b2b;
    --fire-red: #e31e24;
    --faint-red: #d71b21;
    --white: #ffffff;
    --ink: #333333;
    --faint-grey: #ececec;
    --wedge-grey: #8a8a8a;
    --rule: #9a9a9a;
  }
  * { box-sizing: border-box; margin: 0; padding: 0; }
  html, body { width: 1200px; height: 866px; overflow: hidden; background: var(--stage); }
  .stage {
    width: 1200px; height: 866px;
    display: flex; align-items: center; justify-content: center; gap: 40px;
  }
  .card {
    position: relative; width: 540px; height: 310px; overflow: hidden;
    box-shadow: 0 10px 24px rgba(0,0,0,.45);
  }
  .card--front { background: var(--fire-red); color: var(--white); }
  .card--back { background: var(--white); color: var(--ink); }

  .backdrop-name {
    position: absolute; left: 24px; top: 176px;
    font-family: "Montserrat", sans-serif; font-weight: 800;
    font-size: 76px; letter-spacing: -2px; line-height: 1;
    white-space: nowrap; pointer-events: none;
  }
  .card--front .backdrop-name { color: var(--faint-red); }
  .card--back .backdrop-name { color: var(--faint-grey); }

  .wordmark {
    position: absolute; right: 36px; top: 64px;
    font-family: "Montserrat", sans-serif; font-weight: 800;
    font-size: 34px; letter-spacing: 1px; line-height: 1;
  }
  .card--front .wordmark { color: var(--white); }
  .card--back .wordmark { color: var(--fire-red); }

  .details {
    position: absolute; left: 34px; top: 146px;
    font-family: "Arimo", sans-serif; font-size: 12px; line-height: 1.35;
  }
  .company-name {
    font-family: "Montserrat", sans-serif; font-weight: 700;
    font-size: 13px; text-transform: uppercase; letter-spacing: .5px;
    white-space: nowrap;
  }
  .office-phone { font-weight: 700; font-size: 17px; margin: 2px 0 3px; }
  .person-name {
    font-family: "Montserrat", sans-serif; font-weight: 800;
    font-size: 17px; text-transform: uppercase; color: var(--fire-red); letter-spacing: .5px;
  }
  .person-title { font-size: 13px; margin-bottom: 6px; }
  .contact-line { display: flex; align-items: center; gap: 7px; font-size: 13px; }
  .contact-line svg { width: 12px; height: 12px; flex: none; }

  .rule {
    position: absolute; left: 250px; right: 36px; top: 226px; height: 1px;
  }
  .card--front .rule { background: rgba(255,255,255,.4); }
  .card--back .rule { background: var(--rule); }

  .band { position: absolute; left: 0; bottom: 0; width: 540px; height: 40px; }
</style>
</head>
<body>
<main class="stage">

  <section class="card card--front" aria-label="Business card front">
    <div class="backdrop-name" aria-hidden="true">STANBROOK</div>
    <p class="wordmark">STANBROOK</p>
    <div class="details">
      <p class="company-name">Stanbrook Fire Services Pty Ltd</p>
      <p class="office-phone">555.0142.0100</p>
      <p class="contact-line">
        <svg viewBox="0 0 12 12"><rect x="0.5" y="2" width="11" height="8" fill="var(--white)"/><path d="M0.5 2 L6 7 L11.5 2" stroke="var(--fire-red)" fill="none"/></svg>
        info@stanbrook.com
      </p>
      <p class="contact-line">
        <svg viewBox="0 0 12 12"><circle cx="6" cy="6" r="5.2" fill="none" stroke="var(--white)"/><ellipse cx="6" cy="6" rx="2.2" ry="5.2" fill="none" stroke="var(--white)"/><line x1="0.8" y1="6" x2="11.2" y2="6" stroke="var(--white)"/></svg>
        www.stanbrook.com
      </p>
    </div>
    <div class="rule"></div>
  </section>

  <section class="card card--back" aria-label="Business card back">
    <div class="backdrop-name" aria-hidden="true">STANBROOK</div>
    <p class="wordmark">STANBROOK</p>
    <div class="details">
      <p class="person-name">Daniel Hartley</p>
      <p class="person-title">Managing Director</p>
      <p class="contact-line">
        <svg viewBox="0 0 12 12"><rect x="3" y="0.5" width="6.5" height="11" rx="1.2" fill="none" stroke="var(--fire-red)" stroke-width="1.2"/><circle cx="6.25" cy="9.5" r=".7" fill="var(--fire-red)"/></svg>
        555.0187.2234
      </p>
      <p class="contact-line">
        <svg viewBox="0 0 12 12"><rect x="0.5" y="2" width="11" height="8" fill="var(--fire-red)"/><path d="M0.5 2 L6 7 L11.5 2" stroke="var(--white)" fill="none"/></svg>
        daniel@stanbrook.com
      </p>
    </div>
    <div class="rule"></div>
    <svg class="band" viewBox="0 0 540 40" preserveAspectRatio="none" aria-hidden="true">
      <polygon points="0,14 540,36 540,40 0,40" fill="var(--fire-red)"/>
      <polygon points="0,22 260,40 0,40" fill="var(--wedge-grey)"/>
    </svg>
  </section>

</main>
</body>
</html>
```